B2B Energy Broker Website

Our current website looks amateur, we need something far more professional looking and advanced. Current website is www.halvorn-utilitypartners.com

```html
<!DOCTYPE html>
<html lang="en">
<head>
<meta charset="utf-8">
<title>Halvorn Utility Partners</title>
<link href="https://fonts.googleapis.com/css2?family=Poppins:wght@300;400;500;600;700&family=Lato:wght@400;700&display=swap" rel="stylesheet">
<style>
:root{
  --navy:#232a5c;
  --navy-deep:#1d2250;
  --ink:#2b2b2b;
  --text:#444a55;
  --muted:#777d88;
  --line:#e6e7ec;
  --white:#ffffff;
  --grey-logo:#4a4a4a;
}
*{box-sizing:border-box;margin:0;padding:0}
html,body{width:1200px;height:3833px;overflow:hidden}
body{position:relative;background:var(--white);font-family:'Lato',sans-serif;color:var(--text)}
.abs{position:absolute}
.btn{position:absolute;display:flex;align-items:center;justify-content:center;border-radius:30px;font-family:'Poppins',sans-serif;font-weight:600;font-size:15px;color:var(--white);background:var(--navy)}

/* header */
.site-header{position:absolute;left:0;top:0;width:1200px;height:124px;background:var(--white)}
.topbar{position:absolute;left:402px;top:0;width:798px;height:51px;background:var(--navy);color:var(--white);font-family:'Poppins',sans-serif;font-size:15px}
.topbar .item{position:absolute;top:15px;display:flex;align-items:center;gap:10px}
.topbar .social{position:absolute;top:8px;width:36px;height:36px;border-radius:50%;background:var(--white);color:var(--navy);font-size:11px;font-weight:600;display:flex;align-items:center;justify-content:center}
.brand{position:absolute;left:113px;top:27px;display:flex;align-items:center;gap:10px}
.brand .dot{width:68px;height:68px;border-radius:50%;background:var(--grey-logo)}
.brand .name{font-family:'Poppins',sans-serif;color:var(--grey-logo);line-height:1}
.brand .name b{display:block;font-weight:400;font-size:29px;letter-spacing:6px}
.brand .name span{display:block;font-weight:300;font-size:18px;margin-top:6px}
.nav a{position:absolute;top:77px;font-family:'Poppins',sans-serif;font-size:15px;color:var(--ink);text-decoration:none}
.nav a.active{color:var(--navy)}

/* hero */
.hero{position:absolute;left:0;top:124px;width:1200px;height:601px;background:linear-gradient(180deg,#bfc5cb 0%,#9aa1a8 45%,#5b636c 75%,#3a4048 100%)}
.hero h1{position:absolute;left:0;width:1200px;text-align:center;color:var(--white);font-family:'Poppins',sans-serif}
.hero .pre{top:96px;font-weight:300;font-size:33px}
.hero .title{top:150px;font-weight:700;font-size:52px}
.dots{position:absolute;left:578px;top:548px;display:flex;gap:8px;align-items:center}
.dots i{display:block;width:11px;height:11px;border-radius:50%;background:var(--white)}
.dots i.on{width:17px;height:17px;border:3px solid var(--white);background:transparent}

/* headings */
.sec-title{position:absolute;font-family:'Poppins',sans-serif;font-weight:600;color:var(--ink);text-align:center}
.sec-title::after{content:"";display:block;width:42px;height:3px;background:var(--navy);margin:8px auto 0}

/* about */
.about-frame{position:absolute;border-color:var(--navy);border-style:solid}
.about-photo{position:absolute;left:122px;top:822px;width:433px;height:328px;background:linear-gradient(160deg,#3d6fa6 0%,#7fa3c6 40%,#dfe6ee 70%,#f4f6f8 100%)}
.about h2{position:absolute;left:651px;top:822px;font-family:'Poppins',sans-serif;font-weight:600;font-size:30px;color:var(--ink)}
.about h2::after{content:"";display:block;width:100%;height:2px;background:var(--navy);margin-top:4px}
.about p{position:absolute;left:651px;top:892px;width:441px;font-size:14.5px;line-height:25.7px;text-align:justify;color:var(--text)}

/* services */
.services{position:absolute;left:0;top:1243px;width:1200px;height:529px;background:linear-gradient(120deg,#e9e6e3 0%,#d8d2cc 40%,#efece9 70%,#cfc7bf 100%)}
.card{position:absolute;top:151px;width:223px;height:286px;color:var(--white);text-align:center;padding:0 18px}
.card.solid{background:var(--navy)}
.card.tint{background:rgba(40,38,48,.85)}
.card svg{display:block;margin:26px auto 0}
.card h3{font-family:'Poppins',sans-serif;font-weight:600;font-size:15px;line-height:22px;margin-top:14px}
.card p{font-size:13px;line-height:23px;margin-top:6px}

/* why us */
.why .col{position:absolute;top:1948px;width:310px;text-align:center}
.why svg{display:block;margin:0 auto}
.why h3{font-family:'Poppins',sans-serif;font-weight:500;font-size:18px;color:var(--ink);margin-top:42px}
.why p{font-size:13px;line-height:30px;margin-top:10px;color:var(--text)}

/* clients */
.clients{position:absolute;left:0;top:2281px;width:1200px;height:498px;background:linear-gradient(180deg,#2a336b 0%,#2d3670 50%,#343f7c 100%)}
.clients .sec-title{color:var(--white)}
.clients .sec-title::after{background:var(--white)}
.logo-box{position:absolute;width:159px;height:65px;background:var(--white);display:flex;align-items:center;justify-content:center;font-family:'Poppins',sans-serif;font-weight:500;font-size:19px;color:#5a5f6a;clip-path:polygon(0 0,100% 0,100% 72%,86% 100%,0 100%)}
.btn-outline{position:absolute;left:533px;top:374px;width:133px;height:42px;border:2px solid var(--white);border-radius:30px;color:var(--white);font-family:'Poppins',sans-serif;font-weight:600;font-size:14px;display:flex;align-items:center;justify-content:center}

/* faq */
.faq-photo{position:absolute;left:0;top:2918px;width:603px;height:547px;background:linear-gradient(200deg,#f2f3f5 0%,#2f6fc4 45%,#1d3f87 75%,#172f66 100%);clip-path:polygon(38% 0,72% 0,100% 100%,0 100%,0 42%)}
.faq h2{position:absolute;left:576px;top:2858px;font-family:'Poppins',sans-serif;font-weight:600;font-size:28px;color:var(--navy-deep)}
.faq .rule{position:absolute;left:576px;top:2905px;width:96px;height:2px;background:var(--navy)}
.qa{position:absolute;left:578px;width:510px;background:var(--white);box-shadow:0 2px 10px rgba(0,0,0,.08);padding:0 24px}
.qa h4{font-family:'Poppins',sans-serif;font-weight:500;font-size:15px;color:var(--ink);height:63px;display:flex;align-items:center;justify-content:space-between}
.qa h4 span{font-size:20px;color:var(--muted);font-weight:400}
.qa p{font-size:11px;line-height:21px;color:var(--muted);margin-top:-10px}

/* footer */
.site-footer{position:absolute;left:0;top:3465px;width:1200px;height:368px;background:var(--navy-deep);color:var(--white)}
.site-footer h5{position:absolute;top:93px;font-family:'Poppins',sans-serif;font-weight:500;font-size:18px}
.f-brand{position:absolute;left:113px;top:98px;display:flex;align-items:center;gap:10px}
.f-brand .dot{width:68px;height:68px;border-radius:50%;background:var(--white)}
.f-brand .name{font-family:'Poppins',sans-serif;line-height:1}
.f-brand .name b{display:block;font-weight:400;font-size:29px;letter-spacing:6px}
.f-brand .name span{display:block;font-weight:300;font-size:18px;margin-top:6px}
.f-social{position:absolute;top:218px;width:44px;height:44px;border-radius:50%;border:1.5px solid var(--white);display:flex;align-items:center;justify-content:center;font-family:'Poppins',sans-serif;font-size:11px;font-weight:600}
.f-social.fill{background:var(--navy);border-color:var(--navy)}
.f-links{position:absolute;left:384px;top:132px;list-style:none;font-size:15px;line-height:30px}
.f-contact{position:absolute;left:566px;font-size:15px;display:flex;gap:12px;line-height:25px}
.news-input{position:absolute;left:850px;top:135px;width:182px;height:45px;background:var(--white);color:#999;font-size:14px;padding:0 12px;display:flex;align-items:center}
.news-btn{position:absolute;left:1032px;top:135px;width:56px;height:45px;background:#3a4590;display:flex;align-items:center;justify-content:center}
.copy{position:absolute;left:0;top:317px;width:1200px;text-align:center;font-size:14.5px}
</style>
</head>
<body>

<header class="site-header">
  <div class="brand">
    <div class="dot"></div>
    <div class="name"><b>HALVORN</b><span>utility partners</span></div>
  </div>
  <div class="topbar">
    <div class="item" style="left:42px">
      <svg width="16" height="16" viewBox="0 0 24 24" fill="#fff"><path d="M6.6 10.8a15.1 15.1 0 0 0 6.6 6.6l2.2-2.2c.3-.3.7-.4 1-.2 1.1.4 2.3.6 3.6.6.6 0 1 .4 1 1V20c0 .6-.4 1-1 1A17 17 0 0 1 3 4c0-.6.4-1 1-1h3.5c.6 0 1 .4 1 1 0 1.3.2 2.5.6 3.6.1.3 0 .7-.2 1z"/></svg>
      0300 555 0142
    </div>
    <div class="item" style="left:231px">
      <svg width="18" height="14" viewBox="0 0 24 18" fill="#fff"><path d="M2 0h20a2 2 0 0 1 2 2v.5L12 10 0 2.5V2a2 2 0 0 1 2-2zM0 5l12 7.5L24 5v11a2 2 0 0 1-2 2H2a2 2 0 0 1-2-2z"/></svg>
      info@halvornutility.com
    </div>
    <div class="social" style="left:545px">FB</div>
    <div class="social" style="left:586px">TW</div>
    <div class="social" style="left:627px">IG</div>
  </div>
  <nav class="nav">
    <a class="active" style="left:401px">HOME</a>
    <a style="left:491px">ABOUT US</a>
    <a style="left:612px">SERVICES</a>
    <a style="left:730px">FAQ</a>
    <a style="left:806px">CONTACT US</a>
    <svg class="abs" style="left:933px;top:79px" width="16" height="16" viewBox="0 0 24 24" fill="none" stroke="#232a5c" stroke-width="3"><circle cx="10" cy="10" r="7"/><path d="M15 15l6 6"/></svg>
  </nav>
  <div class="btn" style="left:978px;top:66px;width:110px;height:44px">LOG IN</div>
</header>

<section class="hero" role="img" aria-label="Photo of two engineers in hard hats walking between rows of solar panels with wind turbines behind">
  <h1 class="pre">WELCOME TO</h1>
  <h1 class="title">HALVORN UTILITY PARTNERS</h1>
  <div class="dots"><i></i><i class="on"></i><i></i></div>
</section>

<section class="about">
  <div class="about-frame" style="left:479px;top:810px;width:86px;height:84px;border-width:4px 4px 0 0"></div>
  <div class="about-frame" style="left:111px;top:1077px;width:84px;height:82px;border-width:0 0 4px 4px"></div>
  <div class="about-photo" role="img" aria-label="Photo of a snow-covered mountain peak above clouds"></div>
  <h2>ABOUT US</h2>
  <p>Halvorn Utility Partners has been founded on a wealth of 30 years of commercial energy expertise with a mission to provide customers with a fresh approach to business utility services. Developing a large network of over 18 energy suppliers, Halvorn Utility Partners breaks the mould, offering clear and transparent cost reducing solutions in what can be a complicated and overwhelming process. The wholesale power,</p>
  <div class="btn" style="left:651px;top:1100px;width:155px;height:50px">LEARN MORE</div>
</section>

<section class="services" role="img" aria-label="Soft blurred background photo of a hand holding a glowing light bulb">
  <h2 class="sec-title" style="left:0;width:1200px;top:71px;font-size:30px">SERVICES</h2>
  <div class="card solid" style="left:112px">
    <svg width="76" height="70" viewBox="0 0 76 70" fill="none" stroke="#fff" stroke-width="2.5"><path d="M38 6c6 10 14 16 14 28a14 14 0 0 1-28 0c0-7 4-11 6-15 1 5 3 7 6 8-1-8 0-15 2-21z"/><path d="M10 50h56M16 58h44M24 50v8M52 50v8"/></svg>
    <h3>COMMERCIAL GAS</h3>
    <p>We offer an impartial review of your business gas requirements to ensure you are getting the best prices, service and management.</p>
  </div>
  <div class="card tint" style="left:363px">
    <svg width="76" height="70" viewBox="0 0 76 70" fill="none" stroke="#fff" stroke-width="2.5"><path d="M44 4L24 38h14L30 66l22-36H38z"/><path d="M14 20l6 4M12 36h6M58 36h6M56 20l-6 4"/></svg>
    <h3>COMMERCIAL<br>ELECTRICITY</h3>
    <p>We offer an impartial review of your business electricity requirements to ensure you are getting the best prices.</p>
  </div>
  <div class="card solid" style="left:614px">
    <svg width="76" height="70" viewBox="0 0 76 70" fill="none" stroke="#fff" stroke-width="2.5"><circle cx="38" cy="44" r="20"/><path d="M18 44h40M38 24v40M28 26c-4 10-4 26 0 36M48 26c4 10 4 26 0 36"/><path d="M14 8c3 5 6 7 6 12a5 5 0 0 1-10 0c0-4 2-7 4-12zM38 4l-5 9h6l-4 8M62 8c3 5 6 7 6 12a5 5 0 0 1-10 0c0-4 2-7 4-12z"/></svg>
    <h3>UTILITY SERVICES</h3>
    <p>We can provide a wide range of business utility management services to ensure your time and money</p>
  </div>
  <div class="card tint" style="left:866px">
    <svg width="76" height="70" viewBox="0 0 76 70" fill="none" stroke="#fff" stroke-width="2.5"><path d="M38 4C30 18 20 30 20 44a18 18 0 0 0 36 0C56 30 46 18 38 4z"/><path d="M28 46a10 10 0 0 0 10 10"/></svg>
    <h3>COMMERCIAL WATER</h3>
    <p>The commercial water market has now been de-regulated. Speak to our team to find out how we can save you money.</p>
  </div>
</section>

<section class="why">
  <h2 class="sec-title" style="left:0;width:1200px;top:1851px;font-size:29px">WHY US</h2>
  <div class="col" style="left:107px">
    <svg width="90" height="90" viewBox="0 0 90 90" fill="none" stroke="#2b2b2b" stroke-width="2.5"><circle cx="36" cy="34" r="22"/><circle cx="36" cy="34" r="10"/><path d="M30 54v26M40 56v24M66 20v60M60 28l6-8 6 8"/><circle cx="60" cy="62" r="14"/></svg>
    <h3>MARKET TREND ANALYSIS</h3>
    <p>Our energy analysts monitor a live energy market curve to ensure you buy at the right time and save as much possible.</p>
  </div>
  <div class="col" style="left:445px">
    <svg width="90" height="90" viewBox="0 0 90 90" fill="none" stroke="#2b2b2b" stroke-width="2.5"><circle cx="45" cy="42" r="34"/><circle cx="45" cy="28" r="7"/><circle cx="30" cy="34" r="5"/><circle cx="60" cy="34" r="5"/><path d="M32 46c4-6 22-6 26 0M12 58l20 14 12-8 14 10 20-16"/></svg>
    <h3>DIRECT RELATIONSHIPS</h3>
    <p>We hold direct relationships with over 18 major suppliers, we use these relationships to ensure you get the most from your supplier.</p>
  </div>
  <div class="col" style="left:783px">
    <svg width="90" height="90" viewBox="0 0 90 90" fill="none" stroke="#2b2b2b" stroke-width="2.5"><path d="M6 84h78M10 84V44l18 10V44l18 10V44l18 10V20h12v64"/><path d="M18 66h50M18 74h50M54 12c6-6 14-6 20 0s14 6 20 0"/></svg>
    <h3>INDUSTRY EXPERIENCE</h3>
    <p>Our two founders hold over 30 years industry experience between them and our staff are what we believe to be the best in the industry.</p>
  </div>
</section>

<section class="clients" role="img" aria-label="Dark blue tinted photo of a solar farm in open countryside">
  <h2 class="sec-title" style="left:0;width:1200px;top:69px;font-size:28px">OUR CLIENTS</h2>
  <div class="logo-box" style="left:265px;top:161px">Nordvind</div>
  <div class="logo-box" style="left:435px;top:161px">Brightwell</div>
  <div class="logo-box" style="left:606px;top:161px">Kestrel Gas</div>
  <div class="logo-box" style="left:776px;top:161px">Severn</div>
  <div class="logo-box" style="left:265px;top:268px">Envara</div>
  <div class="logo-box" style="left:435px;top:268px">Lumina</div>
  <div class="logo-box" style="left:606px;top:268px">Crestline Gas</div>
  <div class="logo-box" style="left:776px;top:268px;font-size:16px">Highland Power</div>
  <div class="btn-outline">VIEW ALL</div>
</section>

<section class="faq">
  <div class="faq-photo" role="img" aria-label="Photo of a technician in blue overalls and hard hat installing a solar panel with a drill"></div>
  <h2>FREQUENTLY ASKED QUESTIONS</h2>
  <div class="rule"></div>
  <div class="qa" style="top:2951px"><h4>Why Should My Business Use Halvorn Utility Partners?<span>+</span></h4></div>
  <div class="qa" style="top:3029px;height:120px"><h4>Who Should Consider Using Halvorn Utility Partners?<span>–</span></h4>
    <p>Any association, business type, charity, council, not for profit organisation or any other user of energy as paid for by non domestic entity.Any association, business type,</p></div>
  <div class="qa" style="top:3167px"><h4>Is Halvorn Utility Partners Independent?<span>+</span></h4></div>
  <div class="qa" style="top:3244px"><h4>Will There Be A Charge For Gaining Quotations?<span>+</span></h4></div>
  <div class="btn" style="left:762px;top:3344px;width:142px;height:43px;font-size:14px">LOAD MORE</div>
</section>

<footer class="site-footer">
  <div class="f-brand">
    <div class="dot"></div>
    <div class="name"><b>HALVORN</b><span>utility partners</span></div>
  </div>
  <div class="f-social" style="left:113px">FB</div>
  <div class="f-social fill" style="left:173px">TW</div>
  <div class="f-social" style="left:233px">IN</div>
  <div class="f-social" style="left:292px">IG</div>

  <h5 style="left:384px">QUICK LINKS</h5>
  <ul class="f-links"><li>Home</li><li>About Us</li><li>Services</li><li>FAQ</li><li>Contact Us</li></ul>

  <h5 style="left:566px">CONTACT US</h5>
  <div class="f-contact" style="top:130px">
    <svg width="14" height="20" viewBox="0 0 14 20" fill="#fff" style="margin-top:4px"><path d="M7 0a7 7 0 0 0-7 7c0 5 7 13 7 13s7-8 7-13a7 7 0 0 0-7-7zm0 10a3 3 0 1 1 0-6 3 3 0 0 1 0 6z"/></svg>
    <div>12 Marlow Street<br>Leicester, LE1 4QT</div>
  </div>
  <div class="f-contact" style="top:195px">
    <svg width="16" height="16" viewBox="0 0 24 24" fill="#fff" style="margin-top:4px"><path d="M6.6 10.8a15.1 15.1 0 0 0 6.6 6.6l2.2-2.2c.3-.3.7-.4 1-.2 1.1.4 2.3.6 3.6.6.6 0 1 .4 1 1V20c0 .6-.4 1-1 1A17 17 0 0 1 3 4c0-.6.4-1 1-1h3.5c.6 0 1 .4 1 1 0 1.3.2 2.5.6 3.6.1.3 0 .7-.2 1z"/></svg>
    <div>0300 555 0142</div>
  </div>
  <div class="f-contact" style="top:232px">
    <svg width="16" height="12" viewBox="0 0 24 18" fill="#fff" style="margin-top:7px"><path d="M2 0h20a2 2 0 0 1 2 2v.5L12 10 0 2.5V2a2 2 0 0 1 2-2zM0 5l12 7.5L24 5v11a2 2 0 0 1-2 2H2a2 2 0 0 1-2-2z"/></svg>
    <div>info@halvornutility.com</div>
  </div>

  <h5 style="left:850px">SIGN UP FOR NEWSLETTER</h5>
  <div class="news-input">Email Address</div>
  <div class="news-btn"><svg width="18" height="14" viewBox="0 0 24 18" fill="#fff"><path d="M2 0h20a2 2 0 0 1 2 2v.5L12 10 0 2.5V2a2 2 0 0 1 2-2zM0 5l12 7.5L24 5v11a2 2 0 0 1-2 2H2a2 2 0 0 1-2-2z"/></svg></div>

  <div class="copy">©Copyrights 2022 halvornutility &nbsp; | &nbsp; All Rights Reserved</div>
</footer>

</body>
</html>
```